New local Orchid nursery branding

We need a business card designed for our small local company in Darwin, Australia that grows orchids, called Blooms at Carrow.
We will be running private sales from our property, and handing these out at local events for perspective customers.

We would like to see designs that are simple, and able to be used with minimal colours and containing an orchid, preferably a stylised representation instead of a photo.
The eventual hope is to take this into larger formats to create our company logo/branding etc, but for now we just need business cards.

Target Market(s)

Local Orchid

Industry/Entity Type

Business

Contact Information for Business Card

Company Name
Logo
Name
Phone Number
Street Address
Email Address (less prominent than rest of the text)

Font styles to use
Sans Serif

Requirements
Must have
• Name of the company, which is Blooms at Carrow
Nice to have
• stylised orchid logo
Should not have
• too many colours

```html
<!DOCTYPE html>
<html lang="en">
<head>
<meta charset="utf-8">
<title>Blooms at Carrow – Business Card</title>
<link rel="stylesheet" href="https://fonts.googleapis.com/css2?family=Didact+Gothic&display=swap">
<style>
  :root {
    --backdrop: #e9e7ea;
    --card: #ffffff;
    --orchid: #b070b8;
    --orchid-mid: #cf9fd3;
    --orchid-pale: #f1e2f2;
    --ink: #2a1f3d;
    --icon: #3b2a58;
  }
  * { margin: 0; padding: 0; box-sizing: border-box; }
  html, body {
    width: 1200px; height: 720px; overflow: hidden;
    background: var(--backdrop);
  }
  .card {
    position: absolute; left: 75px; top: 60px;
    width: 1050px; height: 600px;
    background: var(--card);
    overflow: hidden;
    box-shadow: 0 6px 24px rgba(40, 20, 50, 0.18);
    font-family: "Didact Gothic", sans-serif;
    color: var(--ink);
  }
  .floral-art { position: absolute; inset: 0; width: 100%; height: 100%; }
  .brand {
    position: absolute; left: 190px; top: 40px;
    color: var(--ink); font-weight: 400;
    display: flex; flex-direction: column; align-items: flex-end;
    line-height: 1;
  }
  .brand-main { font-size: 104px; letter-spacing: 1px; }
  .brand-sub { font-size: 36px; letter-spacing: 4px; margin-top: 2px; }
  .contact-list {
    position: absolute; left: 330px; top: 262px;
    list-style: none;
  }
  .contact-item {
    display: flex; align-items: center;
    font-size: 26px; line-height: 1.2;
    margin-bottom: 12px;
  }
  .contact-item.address { margin-bottom: 34px; }
  .contact-item.phone-lines { align-items: flex-start; }
  .contact-item.email, .contact-item.web { font-size: 24px; margin-bottom: 4px; }
  .contact-icon {
    width: 24px; height: 24px; flex: none;
    margin-right: 16px; margin-top: 3px;
  }
</style>
</head>
<body>
  <main class="card">
    <svg class="floral-art" viewBox="0 0 1050 600" role="img" aria-label="Stylised purple orchid illustration: an orchid bloom with curling leaves at lower left, faint orchid flowers at upper right and a leafy swirl at lower right">
      <defs>
        <linearGradient id="wave-fill" x1="0" y1="0" x2="1" y2="1">
          <stop offset="0" stop-color="var(--orchid-mid)"/>
          <stop offset="0.55" stop-color="var(--orchid)"/>
          <stop offset="1" stop-color="var(--orchid-mid)"/>
        </linearGradient>
        <linearGradient id="corner-fill" x1="1" y1="0" x2="0" y2="1">
          <stop offset="0" stop-color="var(--orchid-mid)"/>
          <stop offset="1" stop-color="var(--orchid-pale)" stop-opacity="0.3"/>
        </linearGradient>
        <radialGradient id="bloom-fill" cx="0.5" cy="0.5" r="0.5">
          <stop offset="0" stop-color="var(--orchid-pale)"/>
          <stop offset="1" stop-color="var(--orchid-mid)"/>
        </radialGradient>
      </defs>
      <path d="M1050 0 L1050 420 C960 380 880 300 840 210 C810 130 830 50 880 0 Z" fill="url(#corner-fill)"/>
      <path d="M0 230 C60 200 150 250 180 330 C210 410 230 470 300 510 C440 570 690 560 840 500 C930 465 990 420 1050 360 L1050 600 L0 600 Z" fill="url(#wave-fill)"/>
      <path d="M0 290 C50 280 110 330 130 400 C150 470 180 530 250 570 L250 600 L0 600 Z" fill="var(--orchid)" opacity="0.5"/>
      <ellipse cx="215" cy="390" rx="62" ry="56" fill="url(#bloom-fill)"/>
    </svg>

    <h1 class="brand">
      <span class="brand-main">Blooms</span>
      <span class="brand-sub">at Carrow</span>
    </h1>

    <ul class="contact-list">
      <li class="contact-item address">
        <svg class="contact-icon" viewBox="0 0 24 24" aria-hidden="true">
          <rect width="24" height="24" rx="3" fill="var(--icon)"/>
          <path d="M12 5a4.5 4.5 0 0 0-4.5 4.5C7.5 13 12 19 12 19s4.5-6 4.5-9.5A4.5 4.5 0 0 0 12 5z" fill="var(--orchid-mid)"/>
          <circle cx="12" cy="9.5" r="1.7" fill="var(--icon)"/>
        </svg>
        <span>company address</span>
      </li>
      <li class="contact-item phone-lines">
        <svg class="contact-icon" viewBox="0 0 24 24" aria-hidden="true">
          <rect width="24" height="24" rx="3" fill="var(--icon)"/>
          <path d="M9 5h3l1 4-2 1c.6 1.6 1.4 2.4 3 3l1-2 4 1v3c0 1-1 2-2 2C11 17 7 13 7 7c0-1 1-2 2-2z" fill="#fff"/>
        </svg>
        <span>0412 738 905<br>08 8927 4411</span>
      </li>
      <li class="contact-item email">
        <svg class="contact-icon" viewBox="0 0 24 24" aria-hidden="true">
          <rect width="24" height="24" rx="3" fill="var(--icon)"/>
          <rect x="5" y="7" width="14" height="10" fill="var(--orchid-mid)"/>
          <path d="M5 7l7 6 7-6" fill="none" stroke="var(--icon)" stroke-width="1.4"/>
        </svg>
        <span>hello@bloomsatcarrow.com.au</span>
      </li>
      <li class="contact-item web">
        <svg class="contact-icon" viewBox="0 0 24 24" aria-hidden="true">
          <rect width="24" height="24" rx="3" fill="var(--icon)"/>
          <circle cx="12" cy="12" r="6" fill="none" stroke="var(--orchid-mid)" stroke-width="1.4"/>
          <path d="M6 12h12M12 6c-3 3-3 9 0 12M12 6c3 3 3 9 0 12" fill="none" stroke="var(--orchid-mid)" stroke-width="1.2"/>
        </svg>
        <span>www.bloomsatcarrow.com.au</span>
      </li>
    </ul>
  </main>
</body>
</html>
```